Tights Color Chart

We Need for a Webshop 3 or 4 different Color Charts to see the Colors of the Tights.

1 Color Chart only with this Colors: black/schwarz, white/weiss,
naturel/natur.

The other 3 or 4 Charts up to your Design!

Total 54 Colors.

The Language must be in English and German.
Each single Color Chart should have rounded Corners see attachment.

Thank you in advance
TOM

Target Market(s)

Woman, Webshop

Requirements
Must have
• the right Colors, English and German, for the Webshop

```html
<!DOCTYPE html>
<html lang="en">
<head>
<meta charset="utf-8">
<title>Tights Colour Chart</title>
<link rel="stylesheet" href="https://fonts.googleapis.com/css2?family=Arimo:wght@400;700&display=swap">
<style>
  :root {
    --page-bg: #ffffff;
    --label-main: #111111;
    --label-sub: #222222;
    --swatch-w: 87px;
    --swatch-h: 60px;
    --col-gap: 23px;
    --row-pitch: 105px;
  }
  html, body {
    margin: 0;
    padding: 0;
    width: 1200px;
    height: 839px;
    overflow: hidden;
    background: var(--page-bg);
    font-family: "Arimo", Arial, sans-serif;
  }
  .colour-chart {
    position: absolute;
    left: 107px;
    top: 114px;
    display: flex;
    gap: 52px;
  }
  .chart-group {
    display: grid;
    grid-template-columns: repeat(3, var(--swatch-w));
    grid-auto-rows: var(--row-pitch);
    column-gap: var(--col-gap);
  }
  .colour-item {
    display: flex;
    flex-direction: column;
    align-items: center;
  }
  .swatch {
    width: var(--swatch-w);
    height: var(--swatch-h);
    border-radius: 12px;
    background: linear-gradient(90deg, var(--from), var(--to));
  }
  .name-en {
    margin-top: 6px;
    font-size: 12.5px;
    font-weight: 700;
    color: var(--label-main);
    line-height: 1.05;
    white-space: nowrap;
  }
  .name-de {
    font-size: 12px;
    font-weight: 400;
    color: var(--label-sub);
    line-height: 1.1;
    white-space: nowrap;
  }
</style>
</head>
<body>
<main class="colour-chart">

  <section class="chart-group chart-group--dark">
    <div class="colour-item"><div class="swatch" style="--from:#3a3a4e;--to:#48475e"></div><span class="name-en">ocean</span><span class="name-de">ozean</span></div>
    <div class="colour-item"><div class="swatch" style="--from:#323a52;--to:#3f4862"></div><span class="name-en">night</span><span class="name-de">nacht</span></div>
    <div class="colour-item"><div class="swatch" style="--from:#3f3350;--to:#4e3f62"></div><span class="name-en">blu marino</span><span class="name-de">blu marino</span></div>

    <div class="colour-item"><div class="swatch" style="--from:#7a6878;--to:#9a8494"></div><span class="name-en">steel</span><span class="name-de">stahl</span></div>
    <div class="colour-item"><div class="swatch" style="--from:#5a4a52;--to:#6e5c64"></div><span class="name-en">gray</span><span class="name-de">grau</span></div>
    <div class="colour-item"><div class="swatch" style="--from:#564a4e;--to:#6a5c60"></div><span class="name-en">graphite</span><span class="name-de">graphit</span></div>

    <div class="colour-item"><div class="swatch" style="--from:#4c4468;--to:#5e5480"></div><span class="name-en">blu marino melange</span><span class="name-de">blu marino melange</span></div>
    <div class="colour-item"><div class="swatch" style="--from:#3a2e42;--to:#4a3c54"></div><span class="name-en">denim</span><span class="name-de">denim</span></div>
    <div class="colour-item"><div class="swatch" style="--from:#505852;--to:#606864"></div><span class="name-en">silver</span><span class="name-de">silber</span></div>

    <div class="colour-item"><div class="swatch" style="--from:#484a4a;--to:#5a5c5c"></div><span class="name-en">smoke</span><span class="name-de">rauch</span></div>
    <div class="colour-item"><div class="swatch" style="--from:#3a3a3a;--to:#484646"></div><span class="name-en">nero</span><span class="name-de">schwarz</span></div>
    <div class="colour-item"><div class="swatch" style="--from:#343232;--to:#444040"></div><span class="name-en">nero melange</span><span class="name-de">schwart melange</span></div>

    <div class="colour-item"><div class="swatch" style="--from:#9a7256;--to:#b48c70"></div><span class="name-en">beige</span><span class="name-de">beige</span></div>
    <div class="colour-item"><div class="swatch" style="--from:#6e5448;--to:#8a6e60"></div><span class="name-en">nugat</span><span class="name-de">novgat</span></div>
    <div class="colour-item"><div class="swatch" style="--from:#806a6a;--to:#9e8282"></div><span class="name-en">cacao</span><span class="name-de">kakao</span></div>

    <div class="colour-item"><div class="swatch" style="--from:#5e3e3e;--to:#724e4c"></div><span class="name-en">bronzo</span><span class="name-de">bronze</span></div>
    <div class="colour-item"><div class="swatch" style="--from:#4a4a2a;--to:#5e5c36"></div><span class="name-en">olive</span><span class="name-de">olive</span></div>
    <div class="colour-item"><div class="swatch" style="--from:#4a6078;--to:#5a7490"></div><span class="name-en">jeans</span><span class="name-de">jeans</span></div>
  </section>

  <section class="chart-group chart-group--bright">
    <div class="colour-item"><div class="swatch" style="--from:#c0449a;--to:#dc5aae"></div><span class="name-en">crocus</span><span class="name-de">krokus</span></div>
    <div class="colour-item"><div class="swatch" style="--from:#c87aa8;--to:#e892bc"></div><span class="name-en">orchidea</span><span class="name-de">orchidea</span></div>
    <div class="colour-item"><div class="swatch" style="--from:#c83c64;--to:#e0567a"></div><span class="name-en">raspberry</span><span class="name-de">himbeer</span></div>

    <div class="colour-item"><div class="swatch" style="--from:#c43c50;--to:#dc5460"></div><span class="name-en">sorbet</span><span class="name-de">sorbet</span></div>
    <div class="colour-item"><div class="swatch" style="--from:#9a3444;--to:#b44854"></div><span class="name-en">lipstic</span><span class="name-de">rot</span></div>
    <div class="colour-item"><div class="swatch" style="--from:#a83c40;--to:#c04e4e"></div><span class="name-en">rosso</span><span class="name-de">rosso</span></div>

    <div class="colour-item"><div class="swatch" style="--from:#4a4c7a;--to:#5e5c90"></div><span class="name-en">baby blue</span><span class="name-de">baby blau</span></div>
    <div class="colour-item"><div class="swatch" style="--from:#8060a8;--to:#9a7cc0"></div><span class="name-en">iris</span><span class="name-de">iris</span></div>
    <div class="colour-item"><div class="swatch" style="--from:#7a3e88;--to:#94509e"></div><span class="name-en">azalea</span><span class="name-de">azalea</span></div>

    <div class="colour-item"><div class="swatch" style="--from:#6e3450;--to:#864460"></div><span class="name-en">mulberry</span><span class="name-de">maulbeere</span></div>
    <div class="colour-item"><div class="swatch" style="--from:#8a2e62;--to:#a23e78"></div><span class="name-en">fuchsia</span><span class="name-de">fuchsia</span></div>
    <div class="colour-item"><div class="swatch" style="--from:#b04878;--to:#c85c8a"></div><span class="name-en">lavende</span><span class="name-de">lavendel</span></div>

    <div class="colour-item"><div class="swatch" style="--from:#6e3048;--to:#88405c"></div><span class="name-en">violet</span><span class="name-de">violett</span></div>
    <div class="colour-item"><div class="swatch" style="--from:#7a4658;--to:#945c70"></div><span class="name-en">prugna</span><span class="name-de">pflaume</span></div>
    <div class="colour-item"><div class="swatch" style="--from:#6e4a62;--to:#86607a"></div><span class="name-en">berry</span><span class="name-de">beerch</span></div>

    <div class="colour-item"><div class="swatch" style="--from:#3a9a4a;--to:#4ab65a"></div><span class="name-en">grass</span><span class="name-de">grassgrün</span></div>
    <div class="colour-item"><div class="swatch" style="--from:#28aa96;--to:#3cc8b0"></div><span class="name-en">lagoon</span><span class="name-de">lagune</span></div>
    <div class="colour-item"><div class="swatch" style="--from:#28b8c4;--to:#30d0d8"></div><span class="name-en">turquoise</span><span class="name-de">türkis</span></div>
  </section>

  <section class="chart-group chart-group--light">
    <div class="colour-item"><div class="swatch" style="--from:#e07830;--to:#e89238"></div><span class="name-en">orange</span><span class="name-de">orange</span></div>
    <div class="colour-item"><div class="swatch" style="--from:#d07870;--to:#e0968e"></div><span class="name-en">salmon</span><span class="name-de">lachs</span></div>
    <div class="colour-item"><div class="swatch" style="--from:#b08878;--to:#c8a898"></div><span class="name-en">naturel</span><span class="name-de">ngtur</span></div>

    <div class="colour-item"><div class="swatch" style="--from:#7ad4c4;--to:#a8ecdc"></div><span class="name-en">aquamarina</span><span class="name-de">aquamarina</span></div>
    <div class="colour-item"><div class="swatch" style="--from:#3ab4b0;--to:#60dcd4"></div><span class="name-en">lazur</span><span class="name-de">lazur</span></div>
    <div class="colour-item"><div class="swatch" style="--from:#88aad8;--to:#b0d0ee"></div><span class="name-en">blue</span><span class="name-de">blau</span></div>

    <div class="colour-item"><div class="swatch" style="--from:#c0d870;--to:#e8f898"></div><span class="name-en">kiwi</span><span class="name-de">kiwi</span></div>
    <div class="colour-item"><div class="swatch" style="--from:#58c068;--to:#80dc88"></div><span class="name-en">verde</span><span class="name-de">grün</span></div>
    <div class="colour-item"><div class="swatch" style="--from:#a890cc;--to:#d0b8e6"></div><span class="name-en">lila</span><span class="name-de">lila</span></div>

    <div class="colour-item"><div class="swatch" style="--from:#e080b8;--to:#f8a8d8"></div><span class="name-en">pink</span><span class="name-de">rosa</span></div>
    <div class="colour-item"><div class="swatch" style="--from:#c8a0b0;--to:#ecd0dc"></div><span class="name-en">rose</span><span class="name-de">hellrosa</span></div>
    <div class="colour-item"><div class="swatch" style="--from:#d0c8cc;--to:#f8f0f4"></div><span class="name-en">baby pink</span><span class="name-de">baby rosa</span></div>

    <div class="colour-item"><div class="swatch" style="--from:#d0d0cc;--to:#fcfcf6"></div><span class="name-en">kalina</span><span class="name-de">kalina</span></div>
    <div class="colour-item"><div class="swatch" style="--from:#e4e8dc;--to:#f4f6ec"></div><span class="name-en">cream</span><span class="name-de">creme</span></div>
    <div class="colour-item"><div class="swatch" style="--from:#c8c8c8;--to:#ffffff"></div><span class="name-en">white</span><span class="name-de">weiss</span></div>

    <div class="colour-item"><div class="swatch" style="--from:#b8bcbc;--to:#dcdede"></div><span class="name-en">ash</span><span class="name-de">asche</span></div>
    <div class="colour-item"><div class="swatch" style="--from:#d8d8d0;--to:#f0f0ea"></div><span class="name-en">perle</span><span class="name-de">perle</span></div>
    <div class="colour-item"><div class="swatch" style="--from:#d8dcd4;--to:#f4f6ee"></div><span class="name-en">ecru</span><span class="name-de">ecru</span></div>
  </section>

</main>
</body>
</html>
```